We need a design for the front page of our website

A redesign of our website front page.
www.brook-lantern.net. We are looking for a cleaner bolder fresher look with the confines of the website header as we are redesigning the whole site.

Industry/Entity Type

Tv

Number of Pages Required

1 page

Colors
ffc214

```html
<!DOCTYPE html>
<html lang="en">
<head>
<meta charset="utf-8">
<title>Brook Lantern – Home</title>
<link href="https://fonts.googleapis.com/css2?family=Noto+Sans:wght@400&family=Saira+Semi+Condensed:wght@400&display=swap" rel="stylesheet">
<style>
  :root {
    --brand-yellow: #ffc214;
    --page-light: #f3f3f3;
    --tile-blue: #4a78a4;
    --tile-green: #64ae35;
    --tile-deep-green: #1e8a30;
    --tile-magenta: #b81253;
    --tile-lilac: #d4c6de;
    --tile-grey: #868686;
    --tile-dark-grey: #777777;
    --tile-mauve: #a096a8;
    --tile-white: #ffffff;
    --footer-maroon: #5a1834;
    --text-dark: #333333;
    --text-light: #ffffff;
    --banner-ink: #0d2a3a;
  }
  * { margin: 0; padding: 0; box-sizing: border-box; }
  html, body { width: 768px; height: 1200px; overflow: hidden; background: var(--page-light); }
  body { font-family: "Noto Sans", Verdana, sans-serif; }
  .page { position: relative; width: 768px; height: 1200px; overflow: hidden; background: var(--page-light); }
  .abs { position: absolute; }

  /* header */
  .header-white { left: 0; top: 0; width: 317px; height: 72px; background: #fff; }
  .header-dark { left: 317px; top: 0; width: 271px; height: 72px; background: linear-gradient(180deg, #1f1f1f, #3a3a3a); }
  .header-yellow { left: 588px; top: 0; width: 180px; height: 72px; background: var(--brand-yellow); }
  .brand { left: 162px; top: 26px; display: flex; align-items: center; gap: 5px; font-size: 11px; color: var(--text-dark); letter-spacing: 0.3px; }
  .brand-mark { width: 12px; height: 12px; background: var(--brand-yellow); }

  .nav-bar { left: 0; top: 72px; width: 768px; height: 39px;
    background: linear-gradient(90deg, #e2e2e2 0%, #c9c9c9 12%, #ececec 30%, #dcdcdc 70%, #f4f4f4 100%); }
  .nav-active { left: 231px; top: 72px; width: 58px; height: 39px; background: linear-gradient(180deg, #9aa2a6, #c7cdd0); }
  .nav-item { position: absolute; top: 88px; font-size: 9px; line-height: 11px; color: var(--text-dark); text-decoration: none; white-space: nowrap; }

  .slider-rule { left: 176px; top: 111px; width: 412px; height: 5px; background: #000; }
  .slider-dots { left: 327px; top: 120px; width: 112px; height: 12px; border-radius: 6px; background: linear-gradient(90deg, transparent, #dde0e3, transparent);
    display: flex; align-items: center; justify-content: center; gap: 10px; }
  .dot { width: 7px; height: 7px; border-radius: 50%; border: 1px solid #999; }
  .dot.is-current { width: 10px; height: 10px; background: #1a2a3a; border: 2px solid #4aa0e0; }

  .banner { left: 177px; top: 137px; width: 411px; height: 191px; overflow: hidden;
    background: linear-gradient(110deg, #cfe04a 0%, #7cc23a 30%, #3d9fb0 60%, #0e5e86 85%, #0a3f62 100%); }
  .banner-screen { left: 207px; top: 45px; width: 193px; height: 110px; background: linear-gradient(135deg, #2d5a3a, #4f93a8 60%, #1b3b2a); border: 3px solid #222; }
  .banner-copy { left: 1px; top: 12px; width: 196px; font-family: "Saira Semi Condensed", "Noto Sans", sans-serif; color: var(--banner-ink); }
  .banner-title { font-size: 25px; line-height: 22.5px; font-weight: 400; white-space: nowrap; }
  .banner-sub { margin-top: 7px; font-size: 12.5px; line-height: 16px; white-space: nowrap; }

  /* mosaic */
  .mosaic { left: 0; top: 344px; width: 768px; height: 655px;
    background: radial-gradient(ellipse at 90% 20%, #ffffff 0%, #c4c4c4 30%, #9a9a9a 70%, #6f6f6f 100%), #a0a0a0; }
  .mosaic::before { content: ""; position: absolute; left: 0; top: 0; width: 200px; height: 655px;
    background: radial-gradient(ellipse at 0% 20%, #ffffff 0%, transparent 70%); }
  .tile { position: absolute; }
  .t-light { background: var(--page-light); }
  .t-white { background: var(--tile-white); }
  .t-blue { background: var(--tile-blue); }
  .t-green { background: var(--tile-green); }
  .t-deep-green { background: var(--tile-deep-green); }
  .t-magenta { background: var(--tile-magenta); }
  .t-lilac { background: var(--tile-lilac); }
  .t-grey { background: var(--tile-grey); }
  .t-dark-grey { background: var(--tile-dark-grey); }
  .t-mauve { background: var(--tile-mauve); }

  /* footer */
  .footer { left: 0; top: 999px; width: 768px; height: 201px;
    background: radial-gradient(ellipse at 50% 30%, #6e2544 0%, var(--footer-maroon) 55%, #3e0f22 100%); color: var(--text-light); }
  .footer-links { position: absolute; left: 165px; top: 34px; list-style: none; font-size: 9px; }
  .footer-links li { position: absolute; left: 0; white-space: nowrap; }
  .newsletter-title { position: absolute; left: 297px; width: 165px; top: 38px; text-align: center; font-size: 9px; }
  .field { position: absolute; top: 54px; height: 13px; background: #fff; color: #222; font-size: 8.5px; line-height: 13px; padding-left: 11px; }
  .follow-title { position: absolute; left: 588px; top: 65px; font-size: 9px; }
  .social { position: absolute; width: 19px; height: 19px; border-radius: 3px; }
  .s-sky { background: #3aa2c8; }
  .s-teal { background: #4aa6d8; }
  .s-navy { background: #3b5ea8; }
  .s-steel { background: #6a8ec8; }
  .s-red { background: #d23a3a; }
</style>
</head>
<body>
<div class="page">
  <header>
    <div class="abs header-white"></div>
    <div class="abs header-dark"></div>
    <div class="abs header-yellow"></div>
    <div class="abs brand"><span class="brand-mark"></span><span>Brook Lantern</span></div>

    <div class="abs nav-bar"></div>
    <div class="abs nav-active"></div>
    <nav>
      <a class="nav-item" style="left:245px">Product</a>
      <a class="nav-item" style="left:300px">About Us</a>
      <a class="nav-item" style="left:349px">About Verano</a>
      <a class="nav-item" style="left:414px">Testimonials</a>
      <a class="nav-item" style="left:477px">News</a>
      <a class="nav-item" style="left:516px">Contact us</a>
    </nav>
  </header>

  <section class="hero">
    <div class="abs slider-rule"></div>
    <div class="abs slider-dots">
      <span class="dot"></span><span class="dot"></span><span class="dot is-current"></span><span class="dot"></span><span class="dot"></span>
    </div>
    <div class="abs banner">
      <div class="abs banner-screen" role="img" aria-label="Flat-screen television showing a tropical fish, with a USB memory stick beside it"></div>
      <div class="abs banner-copy">
        <div class="banner-title">TV'S WITH<br>PERSONAL VIDEO<br>RECORDERS (PVR)</div>
        <div class="banner-sub">EASILY RECORD AND PAUSE LIVE<br>TV WHEN USED WITH A USB<br>MEMORY STICK</div>
      </div>
    </div>
  </section>

  <section class="abs mosaic">
    <div class="tile t-light" style="left:168px;top:0;width:108px;height:107px"></div>
    <div class="tile t-blue" style="left:276px;top:0;width:108px;height:107px"></div>
    <div class="tile t-light" style="left:384px;top:0;width:108px;height:107px"></div>
    <div class="tile t-green" style="left:492px;top:0;width:107px;height:107px"></div>

    <div class="tile t-lilac" style="left:168px;top:107px;width:109px;height:216px"></div>
    <div class="tile t-grey" style="left:277px;top:107px;width:107px;height:108px"></div>
    <div class="tile t-magenta" style="left:384px;top:107px;width:215px;height:108px"></div>

    <div class="tile t-white" style="left:277px;top:215px;width:107px;height:108px"></div>
    <div class="tile t-deep-green" style="left:384px;top:215px;width:107px;height:212px"></div>

    <div class="tile t-dark-grey" style="left:168px;top:323px;width:216px;height:105px"></div>
    <div class="tile t-light" style="left:490px;top:321px;width:108px;height:108px"></div>

    <div class="tile t-white" style="left:274px;top:429px;width:108px;height:107px"></div>
    <div class="tile t-grey" style="left:382px;top:427px;width:108px;height:109px"></div>
    <div class="tile t-blue" style="left:490px;top:429px;width:108px;height:107px"></div>

    <div class="tile t-mauve" style="left:171px;top:536px;width:211px;height:107px"></div>
    <div class="tile t-magenta" style="left:382px;top:536px;width:108px;height:119px"></div>
    <div class="tile t-light" style="left:490px;top:536px;width:108px;height:108px"></div>
    <div class="tile t-green" style="left:490px;top:644px;width:108px;height:11px"></div>
  </section>

  <footer class="abs footer">
    <ul class="footer-links">
      <li style="top:0">Product</li>
      <li style="top:21px">About Us</li>
      <li style="top:44px">About Verano</li>
      <li style="top:66px">Testimonials</li>
      <li style="top:88px">News</li>
      <li style="top:107px">Contact Us</li>
    </ul>
    <div class="newsletter-title">Subscribe Newsletter</div>
    <div class="field" style="left:297px;width:81px">Name</div>
    <div class="field" style="left:381px;width:81px">Email</div>
    <div class="follow-title">Follow US</div>
    <span class="social s-sky" style="left:558px;top:82px"></span>
    <span class="social s-teal" style="left:584px;top:82px"></span>
    <span class="social s-navy" style="left:612px;top:82px"></span>
    <span class="social s-steel" style="left:639px;top:82px"></span>
    <span class="social s-red" style="left:558px;top:107px"></span>
  </footer>
</div>
</body>
</html>
```